Marlow Summit Holdings, LLC

I need a new business card desperately.

Please update my business card. I am looking for a professional modern classy design like the Brightfen Partners card in the attachments.

Industry/Entity Type

Investment

Contact Information for Business Card

Colors

Designer to choose colors to be used in the design.

```html
<!DOCTYPE html>
<html lang="en">
<head>
<meta charset="utf-8">
<title>Marlow Summit Holdings, LLC — Business Card</title>
<link href="https://fonts.googleapis.com/css2?family=Montserrat:wght@600&family=Open+Sans:wght@600;700&display=swap" rel="stylesheet">
<style>
  :root {
    --backdrop: #e4e7ea;
    --card-light: #ffffff;
    --card-dark: #535b66;
    --ink: #4a515b;
    --ink-reverse: #ffffff;
  }
  * { margin: 0; padding: 0; box-sizing: border-box; }
  html, body { width: 1200px; height: 901px; overflow: hidden; }
  body {
    background: var(--backdrop);
    display: flex;
    align-items: center;
    justify-content: center;
    gap: 56px;
    font-family: "Open Sans", Arial, sans-serif;
  }
  .card {
    width: 520px;
    height: 297px;
    position: relative;
    box-shadow: 0 10px 28px rgba(40, 48, 58, 0.18);
  }
  .card--front { background: var(--card-light); color: var(--ink); }
  .card--back { background: var(--card-dark); color: var(--ink-reverse); }

  .brand {
    position: absolute;
    display: flex;
    align-items: center;
  }
  .brand__square {
    width: 58px;
    height: 58px;
    background: currentColor;
    flex: none;
  }
  .brand__divider {
    width: 1.5px;
    height: 82px;
    background: currentColor;
    margin: 0 18px;
    flex: none;
  }
  .brand__name {
    font-family: "Montserrat", Arial, sans-serif;
    font-weight: 600;
    text-transform: uppercase;
    line-height: 1.2;
  }
  .brand__line1 { display: block; font-size: 27px; letter-spacing: 0.5px; }
  .brand__line2 { display: block; font-size: 15px; letter-spacing: 1.5px; }

  .card--front .brand { left: 38px; top: 52px; }
  .card--back .brand { left: 50%; top: 50%; transform: translate(-50%, -50%); }

  .holder {
    position: absolute;
    left: 38px;
    top: 176px;
  }
  .holder__name { font-size: 22px; font-weight: 700; line-height: 1.1; }
  .holder__title { font-size: 12px; font-weight: 600; margin-left: 44px; }

  .contact {
    position: absolute;
    left: 193px;
    top: 160px;
    font-size: 13.5px;
    font-weight: 700;
    line-height: 1.45;
    list-style: none;
  }
</style>
</head>
<body>
  <section class="card card--front" aria-label="Business card front">
    <div class="brand">
      <span class="brand__square"></span>
      <span class="brand__divider"></span>
      <p class="brand__name">
        <span class="brand__line1">Marlow Summit</span>
        <span class="brand__line2">Holdings, LLC</span>
      </p>
    </div>
    <div class="holder">
      <p class="holder__name">Owen R. Hale</p>
      <p class="holder__title">Managing Partner</p>
    </div>
    <ul class="contact">
      <li>2240 Cedar Hollow Lane</li>
      <li>Austin, Tx 78750</li>
      <li>Direct: 512.555.0142</li>
      <li>ohale@marlowsummit.com</li>
    </ul>
  </section>

  <section class="card card--back" aria-label="Business card back">
    <div class="brand">
      <span class="brand__square"></span>
      <span class="brand__divider"></span>
      <p class="brand__name">
        <span class="brand__line1">Marlow Summit</span>
        <span class="brand__line2">Holdings, LLC</span>
      </p>
    </div>
  </section>
</body>
</html>
```